Logo Design with Business Card Project

Attractive Logo with colourful background !
I have uploaded a new image of the updated Home page with the Real Estate landing page for your reference.
We are looking for a Business card design which easily identifies us as a Video classifieds company.

Target Market(s)

20 - 35 yr old people who are connected through social media

Industry/Entity Type

Business

Logo Text

WE SEE ALL

Logo styles of interest
Abstract Logo
Requirements
Must have
• Simple layout with striking / engaging colours
Nice to have
• Require an updated logo to go on business card / home page

```html
<!DOCTYPE html>
<html lang="en">
<head>
<meta charset="utf-8">
<title>WE SEE ALL – Business Card</title>
<link href="https://fonts.googleapis.com/css2?family=Bebas+Neue&family=Ubuntu:wght@400&display=swap" rel="stylesheet">
<style>
  :root {
    --page: #ffffff;
    --card-light: #f2f2f2;
    --card-dark: #222222;
    --teal: #00a096;
    --purple: #9b3f8c;
    --ink: #262626;
    --white: #ffffff;
    --stripe-dark: #5c5c5c;
    --stripe-light: #bcbcbc;
    --stripe-mid: #8f8f8f;
    --lens-dark: #2e2e2e;
    --label: #1f5aa8;
  }
  html, body {
    margin: 0;
    padding: 0;
    width: 1200px;
    height: 981px;
    overflow: hidden;
    background: var(--page);
  }
  .canvas {
    position: relative;
    width: 1200px;
    height: 981px;
  }
  .card {
    position: absolute;
    top: 27px;
    width: 486px;
    height: 809px;
    overflow: hidden;
  }
  .card--front { left: 75px; background: var(--card-light); }
  .card--back { left: 640px; background: var(--card-dark); }

  .bar { position: absolute; }
  .bar--teal { background: var(--teal); }
  .bar--purple { background: var(--purple); }
  .bar--black { background: var(--card-dark); }
  .bar--grey-dark { background: var(--stripe-dark); }
  .bar--grey-light { background: var(--stripe-light); }
  .bar--grey-mid { background: var(--stripe-mid); }

  .holder-name {
    position: absolute;
    left: 49px;
    top: 106px;
    margin: 0;
    font-family: "Bebas Neue", sans-serif;
    font-size: 37px;
    line-height: 1;
    font-weight: 400;
    color: var(--ink);
    letter-spacing: 0.2px;
  }
  .holder-title {
    position: absolute;
    left: 49px;
    top: 138px;
    margin: 0;
    font-family: "Bebas Neue", sans-serif;
    font-size: 18px;
    line-height: 1;
    color: var(--ink);
    letter-spacing: 0.3px;
  }

  .brand-band {
    position: absolute;
    left: 152px;
    top: 510px;
    width: 334px;
    height: 66px;
    background: var(--teal);
  }
  .brand-dot {
    position: absolute;
    border-radius: 50%;
    background: var(--lens-dark);
  }
  .brand-name {
    position: absolute;
    margin: 0;
    font-family: "Bebas Neue", sans-serif;
    font-weight: 400;
    line-height: 1;
    color: var(--white);
    white-space: nowrap;
  }
  .brand-name--front { left: 278px; top: 520px; font-size: 50px; }
  .brand-name--back { left: 286px; top: 381px; font-size: 46px; }

  .contact {
    position: absolute;
    left: 204px;
    top: 592px;
    margin: 0;
    padding: 0;
    list-style: none;
    font-family: "Ubuntu", sans-serif;
    font-size: 18px;
    color: var(--ink);
  }
  .contact li { height: 36px; line-height: 26px; }

  .tagline {
    position: absolute;
    left: 286px;
    top: 429px;
    margin: 0;
    font-family: "Ubuntu", sans-serif;
    font-size: 15.5px;
    line-height: 22px;
    color: var(--white);
  }
  .tagline__accent { display: block; color: var(--teal); font-size: 16.5px; }

  .side-label {
    position: absolute;
    top: 872px;
    width: 200px;
    margin: 0;
    text-align: center;
    font-family: "Bebas Neue", sans-serif;
    font-size: 23px;
    color: var(--label);
  }
  .side-label--front { left: 218px; }
  .side-label--back { left: 782px; }
</style>
</head>
<body>
<main class="canvas">

  <section class="card card--front" aria-label="Card front">
    <div class="bar bar--teal" style="left:56px; top:0; width:24px; height:85px;"></div>
    <div class="bar bar--purple" style="left:84px; top:0; width:25px; height:85px;"></div>
    <div class="bar bar--teal" style="left:113px; top:0; width:24px; height:85px;"></div>

    <h1 class="holder-name">Daniel Hartwell</h1>
    <p class="holder-title">Managing Director</p>

    <div class="bar bar--teal" style="left:56px; top:178px; width:24px; height:181px;"></div>
    <div class="bar bar--black" style="left:56px; top:364px; width:24px; height:445px;"></div>
    <div class="bar bar--purple" style="left:84px; top:178px; width:25px; height:399px;"></div>
    <div class="bar bar--black" style="left:84px; top:581px; width:25px; height:228px;"></div>
    <div class="bar bar--teal" style="left:113px; top:178px; width:24px; height:306px;"></div>
    <div class="bar bar--black" style="left:113px; top:489px; width:24px; height:320px;"></div>

    <div class="brand-band"></div>
    <div class="brand-dot" style="left:178px; top:495px; width:92px; height:92px;"></div>
    <p class="brand-name brand-name--front">WE SEE ALL</p>

    <ul class="contact">
      <li>M: 0400 555 017</li>
      <li>Ph: +617 5550 1234</li>
      <li>E: daniel@weseeall.com</li>
      <li>www.weseeall.com</li>
    </ul>
  </section>

  <section class="card card--back" aria-label="Card back">
    <div class="bar bar--grey-dark" style="left:196px; top:0; width:23px; height:348px;"></div>
    <div class="bar bar--grey-light" style="left:224px; top:0; width:24px; height:348px;"></div>
    <div class="bar bar--grey-mid" style="left:253px; top:0; width:24px; height:348px;"></div>

    <div class="brand-dot" style="left:194px; top:361px; width:84px; height:84px; background:#3a3a3a;"></div>
    <p class="brand-name brand-name--back">WE SEE ALL</p>
    <p class="tagline">buy and sell through<span class="tagline__accent">#1 Video Classifieds</span></p>

    <div class="bar bar--grey-dark" style="left:196px; top:461px; width:23px; height:348px;"></div>
    <div class="bar bar--grey-light" style="left:224px; top:461px; width:24px; height:348px;"></div>
    <div class="bar bar--grey-mid" style="left:253px; top:461px; width:24px; height:348px;"></div>
  </section>

  <p class="side-label side-label--front">Front</p>
  <p class="side-label side-label--back">Back</p>

</main>
</body>
</html>
```